Hawaiian fusion restaurant seeks new website design for upcoming 15th anniversary

We currently have a website-- moravetacoastkitchen.com-- but it's boring and we really want something exciting and fresh.

Coding

Coded - Design and coding required

Number of Pages Required

1 page

Font styles to use
Serif
Sans Serif

Colors
00AB8E
00BBA5
67D7C9
C6EFE9
E9F9F6
59FF00
82FF00
B8FF75
E3FFCB
F4FFEA
F0912C
F2A743
F7CA91
FBE8D2
FDF5EE

```html
<!DOCTYPE html>
<html lang="en">
<head>
<meta charset="utf-8">
<title>Moraveta Coast Kitchen</title>
<link rel="stylesheet" href="https://fonts.googleapis.com/css2?family=Josefin+Sans:wght@400;600&family=Monoton&family=Montserrat:wght@400;500&family=Oswald:wght@300;400;500;600&display=swap">
<style>
:root{
  --teal:#00AB8E;
  --teal-2:#00BBA5;
  --teal-soft:#67D7C9;
  --teal-mist:#E9F9F6;
  --lime:#82FF00;
  --lime-soft:#B8FF75;
  --lime-mist:#F4FFEA;
  --orange:#F0912C;
  --orange-2:#F2A743;
  --orange-mist:#FDF5EE;
  --ink:#111111;
  --muted:#8a8a8a;
  --night:#0d1a1f;
  --hero:#21434a;
  --tile-dark:#10262b;
  --line:#d9d9d9;
  --white:#ffffff;
}
*{box-sizing:border-box;margin:0;padding:0}
html,body{width:1200px;height:3645px;overflow:hidden;background:var(--white)}
body{position:relative;font-family:"Montserrat",sans-serif;color:var(--ink)}
.abs{position:absolute}
a{color:inherit;text-decoration:none}

/* buttons */
.btn{position:absolute;display:flex;align-items:center;justify-content:center;gap:8px;
  border:2px solid;border-image:linear-gradient(90deg,var(--teal),var(--orange)) 1;
  font-family:"Oswald",sans-serif;font-weight:500;font-size:14px;letter-spacing:2.5px;
  color:var(--orange);background:transparent;white-space:nowrap}
.btn svg{width:16px;height:10px}

/* top bar & header */
.topbar{top:10px;right:158px;font-family:"Oswald",sans-serif;font-weight:300;font-size:12.5px;color:#777;display:flex;gap:14px}
.topbar span.sep{color:var(--teal-soft)}
.header-rule{top:36px;left:0;width:1200px;height:1px;background:var(--teal-mist)}
.brand{display:flex;align-items:center;gap:10px}
.brand-dot{border-radius:50%;background:var(--orange)}
.brand-name{font-family:"Oswald",sans-serif;font-weight:500;font-size:17px;color:var(--teal);line-height:1.05}
.nav{font-family:"Oswald",sans-serif;font-weight:300;font-size:14.5px;color:#444}
.nav a{position:absolute;white-space:nowrap}
.nav a.active{color:var(--teal)}

/* hero */
.hero{top:109px;left:0;width:1200px;height:456px;background:radial-gradient(circle at 50% 48%,#7a5a3c 0%,#3c4f4c 32%,var(--hero) 65%)}
.hero-title{position:absolute;top:125px;left:0;width:1200px;text-align:center;font-family:"Monoton",sans-serif;font-weight:400;font-size:50px;line-height:66px;color:var(--white);letter-spacing:1px}

/* intro */
.eyebrow{font-family:"Oswald",sans-serif;font-weight:300;font-size:19px;color:var(--teal);text-transform:uppercase}
.display{font-family:"Josefin Sans",sans-serif;font-weight:600;color:var(--ink)}
.lede{font-size:15px;line-height:23px;color:#333}
.photo{position:absolute}
.rounded-tlbr{border-radius:28px 0 28px 0}
.salad-fly{top:565px;left:880px;width:320px;height:420px;background:radial-gradient(ellipse at 60% 55%,var(--lime-soft) 0%,var(--lime-mist) 40%,rgba(255,255,255,0) 70%)}

/* menu */
.menu-band{top:1274px;left:0;width:1200px;height:466px;background:radial-gradient(ellipse at 30% 50%,var(--teal-mist) 0%,#f6fcfb 45%,#ffffff 78%)}
.menu-col{position:absolute;width:421px}
.menu-kicker{text-align:center;font-family:"Oswald",sans-serif;font-weight:500;font-size:13px;letter-spacing:1.8px;color:var(--orange)}
.menu-title{text-align:center;font-family:"Oswald",sans-serif;font-weight:500;font-size:24px;letter-spacing:3px;margin-top:4px}
.menu-item{position:absolute;left:0;width:421px}
.menu-row{display:flex;align-items:baseline;gap:12px;font-size:18px;font-weight:400}
.menu-row .dots{flex:1;border-bottom:1px solid var(--line);transform:translateY(-6px)}
.menu-row .price{color:var(--teal)}
.menu-desc{font-size:12.5px;color:var(--muted);margin-top:6px}

/* gallery */
.gallery{top:1783px;left:0;width:1200px;height:508px}
.tile{position:absolute;overflow:hidden}
.tile-copy{position:absolute;font-family:"Oswald",sans-serif;font-weight:300;color:var(--white)}
.tile-copy .kick{font-size:13px;letter-spacing:.5px}
.tile-copy .head{font-size:16.5px;line-height:19px;margin-top:16px;letter-spacing:.5px}
.tile-copy .more{display:inline-block;font-size:12.5px;margin-top:14px;border-bottom:1px solid currentColor;letter-spacing:.5px}
.tile-center{left:0;right:0;text-align:center}

/* philosophy */
.philo-bg{top:2405px;left:820px;width:380px;height:600px;background:radial-gradient(ellipse at 60% 70%,var(--lime-soft) 0%,var(--teal-mist) 35%,#f3f8f7 58%,rgba(255,255,255,0) 80%)}
.kicker-bold{font-family:"Oswald",sans-serif;font-weight:500;font-size:13.5px;letter-spacing:.8px;color:var(--orange)}

/* booking */
.booking{top:2996px;left:0;width:957px;height:319px;background:var(--night);border-top-right-radius:66px}
.booking h2{position:absolute;top:55px;left:157px;font-family:"Oswald",sans-serif;font-weight:300;font-size:38px;color:var(--white);letter-spacing:-.5px}
.booking p{position:absolute;top:108px;left:157px;width:640px;font-size:14px;line-height:22px;color:#e6e6e6}
.field{position:absolute;top:172px;height:26px;border-bottom:1px solid var(--teal-soft);font-size:13px;color:var(--white);display:flex;justify-content:space-between;align-items:center}
.field svg{width:12px;height:8px}
.booking .btn{border-image:linear-gradient(90deg,var(--lime),var(--orange)) 1;color:var(--lime-soft)}

/* footer */
.foot-nav{font-size:21px;color:#333}
.social{display:flex;gap:16px}
.social span{width:20px;height:20px;border:1px solid var(--teal);border-radius:50%;display:block;position:relative}
.social span::after{content:"";position:absolute;left:6px;top:6px;width:6px;height:6px;border-radius:50%;background:var(--teal)}
.copyright{top:3592px;left:0;width:1200px;height:53px;background:var(--night);color:#ddd;text-align:center;font-family:"Oswald",sans-serif;font-weight:300;font-size:14px;line-height:53px;border-top:3px solid var(--teal)}
</style>
</head>
<body>

<!-- Header -->
<div class="abs topbar">
  <span>Harbor Ln, Kailua Bay, HI 96734</span><span class="sep">|</span>
  <span>+1-808-555-0147</span><span class="sep">|</span>
  <span>booking@moravetacoastkitchen.com</span>
</div>
<div class="abs header-rule"></div>
<div class="abs brand" style="top:40px;left:151px">
  <span class="brand-dot" style="width:56px;height:56px"></span>
  <span class="brand-name">Moraveta<br>Coast Kitchen</span>
</div>
<nav class="nav">
  <a class="active" style="top:63px;left:447px">HOME</a>
  <a style="top:63px;left:515px">MENUS</a>
  <a style="top:63px;left:589px">PAGES</a>
  <a style="top:63px;left:659px">BLOG</a>
  <a style="top:63px;left:723px">SHOP</a>
</nav>
<a class="btn" style="top:54px;left:865px;width:176px;height:38px">FIND A TABLE
  <svg viewBox="0 0 16 10"><path d="M0 5h14M10 1l4 4-4 4" stroke="currentColor" stroke-width="1.6" fill="none"/></svg></a>

<!-- Hero -->
<section class="abs hero" role="img" aria-label="Cooked breakfast in a dark pan with bacon, sausages, beans, tomato and a fried egg">
  <h1 class="hero-title">DELICIOUS FOOD<br>&amp; WONDERFUL EATING<br>EXPERIENCE</h1>
</section>

<!-- Intro -->
<div class="abs salad-fly" role="img" aria-label="Fresh salad leaves and vegetables flying out of a white bowl"></div>
<div class="abs eyebrow" style="top:678px;left:157px">Refresh your taste buds</div>
<h2 class="abs display" style="top:712px;left:155px;font-size:41px;line-height:44px">Enjoy An Exceptional<br>Journey of Taste</h2>
<p class="abs lede" style="top:820px;left:157px;width:412px">Lorem ipsum dolor sit amet, consectetur adipis cing elit, sed do eiusmod tempor incididunt ut labore et dolore magna aliqua ut eni...</p>
<a class="btn" style="top:921px;left:157px;width:177px;height:38px">FIND A TABLE
  <svg viewBox="0 0 16 10"><path d="M0 5h14M10 1l4 4-4 4" stroke="currentColor" stroke-width="1.6" fill="none"/></svg></a>
<div class="photo rounded-tlbr" style="top:1002px;left:348px;width:280px;height:228px;background:linear-gradient(135deg,#3a1d16,#7a3a2a 50%,#4f6a2a)" role="img" aria-label="Sliced medium-rare steak with dipping sauce and greens"></div>
<div class="photo rounded-tlbr" style="top:664px;left:659px;width:371px;height:566px;background:linear-gradient(160deg,#2a2a2e 0%,#c46a6f 35%,#d98a86 55%,#3d5a2c 80%,#1d1d20);box-shadow:0 12px 24px rgba(0,0,0,.15)" role="img" aria-label="Seared sesame tuna slices with lemon and salad on a dark plate"></div>

<!-- Menu -->
<section class="abs menu-band">
  <div class="menu-col" style="top:58px;left:157px">
    <div class="menu-kicker">SED UT PERSPICIATIS</div>
    <div class="menu-title">SED UT PERSPICIATIS UN</div>
  </div>
  <div class="menu-col" style="top:58px;left:620px">
    <div class="menu-kicker">SED UT PERSPICIATIS</div>
    <div class="menu-title">SED UT PERSPICIATIS UN</div>
  </div>

  <div class="menu-col" style="top:138px;left:157px;height:300px">
    <div class="menu-item" style="top:0"><div class="menu-row"><span>Quis autem vel emiu</span><span class="dots"></span><span class="price">$36</span></div><div class="menu-desc">Sed ut perspiciatis unde omnis iste natu...</div></div>
    <div class="menu-item" style="top:68px"><div class="menu-row"><span>Dolore mnam aliqu</span><span class="dots"></span><span class="price">$30</span></div><div class="menu-desc">Sed ut perspiciatis unde omnis iste natu...</div></div>
    <div class="menu-item" style="top:133px"><div class="menu-row"><span>Excepteur sint occ</span><span class="dots"></span><span class="price">$59</span></div><div class="menu-desc">Sed ut perspiciatis unde omnis iste natu...</div></div>
    <div class="menu-item" style="top:202px"><div class="menu-row"><span>tatem acantium dol</span><span class="dots"></span><span class="price">$18</span></div><div class="menu-desc">Sed ut perspiciatis unde omnis iste natu...</div></div>
  </div>
  <div class="menu-col" style="top:138px;left:620px;height:300px">
    <div class="menu-item" style="top:0"><div class="menu-row"><span>Quis autem vel emiu</span><span class="dots"></span><span class="price">$36</span></div><div class="menu-desc">Sed ut perspiciatis unde omnis iste natu...</div></div>
    <div class="menu-item" style="top:68px"><div class="menu-row"><span>Dolore mnam aliqu</span><span class="dots"></span><span class="price">$30</span></div><div class="menu-desc">Sed ut perspiciatis unde omnis iste natu...</div></div>
    <div class="menu-item" style="top:133px"><div class="menu-row"><span>Excepteur sint occ</span><span class="dots"></span><span class="price">$59</span></div><div class="menu-desc">Sed ut perspiciatis unde omnis iste natu...</div></div>
    <div class="menu-item" style="top:202px"><div class="menu-row"><span>tatem acantium dol</span><span class="dots"></span><span class="price">$18</span></div><div class="menu-desc">Sed ut perspiciatis unde omnis iste natu...</div></div>
  </div>
</section>

<!-- Gallery -->
<section class="abs gallery">
  <div class="tile" style="left:0;top:0;width:441px;height:508px;background:linear-gradient(160deg,#5b4a3f 0%,#8a6a55 30%,#3a2620 65%,#10262b)" role="img" aria-label="Charcuterie board with cured meats, cheeses and tomatoes">
    <div class="tile-copy" style="left:58px;top:362px">
      <div style="font-family:'Montserrat',sans-serif;font-size:17px;font-weight:400">SED UT PERSP</div>
      <div style="font-family:'Oswald',sans-serif;font-weight:500;font-size:33px;line-height:38px;margin-top:2px;letter-spacing:.5px">Inventore vertis etsi...</div>
      <div class="more" style="color:var(--lime);margin-top:18px">LEARN MORE...</div>
    </div>
  </div>
  <div class="tile" style="left:441px;top:0;width:254px;height:255px;background:linear-gradient(135deg,#3a1d16,#7a3a2a 55%,#4f6a2a)" role="img" aria-label="Sliced steak with dipping sauce"></div>
  <div class="tile" style="left:695px;top:0;width:253px;height:255px;background:var(--tile-dark)">
    <div class="tile-copy tile-center" style="top:76px"><div class="kick">DOLOREM IPSUM</div><div class="head">QUIS AUTEM VEL EUM IU<br>RE REPREHE NDE</div><div class="more" style="color:var(--teal-soft)">LEARN MORE...</div></div>
  </div>
  <div class="tile" style="left:441px;top:255px;width:254px;height:253px;background:linear-gradient(160deg,var(--orange-2) 0%,var(--orange) 45%,var(--teal) 100%)">
    <div class="tile-copy tile-center" style="top:76px;color:var(--white)"><div class="kick">DOLOREM IPSUM</div><div class="head">QUIS AUTEM VEL EUM IU<br>RE REPREHE NDE</div><div class="more">LEARN MORE...</div></div>
  </div>
  <div class="tile" style="left:695px;top:255px;width:253px;height:253px;background:radial-gradient(ellipse at 50% 50%,#3a2a22 0%,#6b5040 35%,#e8e2da 70%)" role="img" aria-label="Grilled glazed fish on white rice with herbs"></div>
  <div class="tile" style="left:948px;top:0;width:252px;height:508px;background:linear-gradient(180deg,#cfcfcf 0%,#5a4535 25%,#4f5a55 55%,#10262b 85%)" role="img" aria-label="Takeaway boxes with grilled meat, rice and salad">
    <div class="tile-copy" style="left:37px;top:368px"><div class="kick">DOLOREM IPSUM</div><div class="head">QUIS AUTEM VEL EUM IU<br>RE REPREHE NDE</div><div class="more" style="color:var(--teal-soft)">LEARN MORE...</div></div>
  </div>
</section>

<!-- Philosophy -->
<div class="abs philo-bg" role="img" aria-label="Bowl of fresh salad with lemon and chickpeas on a pale stone table"></div>
<div class="photo" style="top:2575px;left:157px;width:250px;height:305px;background:linear-gradient(160deg,#6b1e22 0%,#c9c2a8 40%,#4a4a2a 75%,#2a2a1a)" role="img" aria-label="Poke bowl with tuna and salad"></div>
<div class="photo" style="top:2397px;left:270px;width:316px;height:410px;background:linear-gradient(180deg,#3a2a22 0%,#e9e6e2 30%,#c98a5a 55%,#4f7a2a 80%,#ece9e4);box-shadow:0 10px 24px rgba(0,0,0,.18)" role="img" aria-label="Plate of shredded pork with rice, greens and carrot"></div>
<div class="abs kicker-bold" style="top:2478px;left:638px">QUALITY &amp; BALANCE</div>
<h2 class="abs display" style="top:2504px;left:637px;font-size:41px;font-weight:400;white-space:nowrap">Our Food Philosophy</h2>
<p class="abs lede" style="top:2565px;left:638px;width:372px;font-size:14.5px;line-height:22px">Lorem ipsum dolor sit amet, consectetur adipis cing elit, sed do eiusmod tempor incididunt ut labore et dolore magna aliqua ut enim ad...</p>
<a class="btn" style="top:2663px;left:642px;width:169px;height:38px">LEARN MORE
  <svg viewBox="0 0 16 10"><path d="M0 5h14M10 1l4 4-4 4" stroke="currentColor" stroke-width="1.6" fill="none"/></svg></a>

<!-- Booking -->
<section class="abs booking">
  <h2>BOOK A TABLE</h2>
  <p>Lorem ipsum dolor sit amet, consectetur adipiscing elit, sed do eiusmod tempor incidi dunt ut labore et dolore magna aliqua ut enim ad...</p>
  <div class="field" style="left:157px;width:232px"><span>1 Person</span><svg viewBox="0 0 12 8"><path d="M1 1l5 5 5-5" stroke="#fff" stroke-width="1.4" fill="none"/></svg></div>
  <div class="field" style="left:412px;width:233px"><span>2022/07/16</span><svg viewBox="0 0 12 8"><path d="M1 1l5 5 5-5" stroke="#fff" stroke-width="1.4" fill="none"/></svg></div>
  <div class="field" style="left:675px;width:235px"><span>9.00AM</span><svg viewBox="0 0 12 8"><path d="M1 1l5 5 5-5" stroke="#fff" stroke-width="1.4" fill="none"/></svg></div>
  <a class="btn" style="top:216px;left:157px;width:177px;height:38px">FIND A TABLE
    <svg viewBox="0 0 16 10"><path d="M0 5h14M10 1l4 4-4 4" stroke="currentColor" stroke-width="1.6" fill="none"/></svg></a>
</section>

<!-- Footer -->
<div class="abs brand" style="top:3410px;left:160px">
  <span class="brand-dot" style="width:64px;height:64px"></span>
  <span class="brand-name">Moraveta<br>Coast Kitchen</span>
</div>
<nav class="nav foot-nav">
  <a class="active" style="top:3432px;left:383px">HOME</a>
  <a style="top:3432px;left:475px">MENUS</a>
  <a style="top:3432px;left:576px">PAGES</a>
  <a style="top:3432px;left:668px">BLOG</a>
  <a style="top:3432px;left:758px">SHOP</a>
</nav>
<a class="btn" style="top:3429px;left:865px;width:176px;height:38px">FIND A TABLE
  <svg viewBox="0 0 16 10"><path d="M0 5h14M10 1l4 4-4 4" stroke="currentColor" stroke-width="1.6" fill="none"/></svg></a>
<div class="abs social" style="top:3502px;left:389px" aria-label="Social links"><span></span><span></span><span></span><span></span></div>
<div class="abs copyright">© Copyright 2022. All rights reserved.</div>

</body>
</html>
```